CD cover/promotional graphic for a new single

I had this up as a project already and I decided to change the image and start a new campaign. So, please use this image and manipulate it whatever way you want, however I’m looking for something impactful, in your face, and mind blowing. Please include the title ‘Quiet Harbor Drift’ and the artist ‘Marcus Pellworth’ on it. Extra points if you can add a tad more burnout smoke in a tasteful way. I’ve also attached the song. Thank you.

```html
<!DOCTYPE html>
<html lang="en">
<head>
<meta charset="utf-8">
<title>Quiet Harbor Drift — Marcus Pellworth</title>
<link rel="stylesheet" href="https://fonts.googleapis.com/css2?family=Kanit:ital,wght@1,800;1,900&family=Oswald:wght@500&display=swap">
<style>
  :root {
    --page: #ffffff;
    --orange-hot: #f4622a;
    --orange-deep: #d8401d;
    --red: #b3261a;
    --red-dark: #6e1d16;
    --black: #0e0d0d;
    --asphalt: #2a2322;
    --title-top: #ffc23a;
    --title-bottom: #f56a1e;
    --title-edge: #a81d12;
    --white: #ffffff;
    --artist: #f7862c;
  }
  html, body {
    margin: 0;
    width: 1200px;
    height: 1000px;
    overflow: hidden;
    background: var(--page);
  }
  .canvas {
    position: relative;
    width: 1200px;
    height: 1000px;
  }
  .cover {
    position: absolute;
    left: 195px;
    top: 105px;
    width: 810px;
    height: 812px;
    overflow: hidden;
    background: linear-gradient(180deg, var(--orange-deep) 0%, var(--red) 45%, var(--red-dark) 75%, var(--black) 100%);
  }
  .cover-shapes {
    position: absolute;
    inset: 0;
  }
  .car-photo {
    position: absolute;
    left: 0;
    top: 380px;
    width: 810px;
    height: 432px;
    background:
      radial-gradient(ellipse 30% 22% at 78% 72%, rgba(200,190,190,0.45) 0%, rgba(200,190,190,0) 100%),
      radial-gradient(ellipse 30% 20% at 40% 80%, rgba(170,160,170,0.4) 0%, rgba(170,160,170,0) 100%),
      radial-gradient(ellipse 50% 30% at 48% 38%, #d6321f 0%, #a81e16 50%, rgba(120,25,20,0) 100%),
      linear-gradient(180deg, rgba(60,25,22,0) 0%, rgba(50,38,38,0.55) 55%, rgba(30,24,24,0.9) 80%, var(--black) 100%);
  }
  .title {
    position: absolute;
    left: 0;
    top: 95px;
    width: 810px;
    margin: 0;
    text-align: center;
    font-family: "Kanit", sans-serif;
    font-style: italic;
    font-weight: 900;
    text-transform: uppercase;
    line-height: 1;
  }
  .title-word {
    display: block;
  }
  .title-word--big {
    font-size: 118px;
    letter-spacing: 2px;
    background: linear-gradient(180deg, var(--title-top) 0%, var(--title-bottom) 100%);
    -webkit-background-clip: text;
    background-clip: text;
    color: transparent;
    filter: drop-shadow(4px 5px 0 var(--title-edge));
  }
  .title-word--small {
    font-size: 58px;
    font-weight: 800;
    color: var(--white);
    margin: -8px 0 -6px;
    filter: drop-shadow(3px 4px 0 var(--title-edge));
  }
  .artist {
    position: absolute;
    left: 0;
    bottom: 52px;
    width: 810px;
    margin: 0;
    text-align: center;
    font-family: "Oswald", sans-serif;
    font-weight: 500;
    font-size: 32px;
    letter-spacing: 8px;
    color: var(--artist);
    text-transform: uppercase;
  }
</style>
</head>
<body>
<main class="canvas">
  <section class="cover">
    <svg class="cover-shapes" width="810" height="812" viewBox="0 0 810 812" aria-hidden="true">
      <defs>
        <linearGradient id="band-glow" x1="0" y1="0" x2="1" y2="1">
          <stop offset="0" stop-color="#f4622a" stop-opacity="0.85"/>
          <stop offset="1" stop-color="#c8311c" stop-opacity="0"/>
        </linearGradient>
        <linearGradient id="chevron-fill" x1="0" y1="0" x2="1" y2="0">
          <stop offset="0" stop-color="#c82a1a"/>
          <stop offset="1" stop-color="#f4582a"/>
        </linearGradient>
        <linearGradient id="black-fade" x1="0" y1="0" x2="0" y2="1">
          <stop offset="0" stop-color="#0e0d0d"/>
          <stop offset="0.7" stop-color="#141111"/>
          <stop offset="1" stop-color="#1c1515" stop-opacity="0.6"/>
        </linearGradient>
      </defs>
      <polygon class="band band--light" points="0,0 300,0 0,300" fill="url(#band-glow)"/>
      <polygon class="band band--shade" points="540,0 720,0 0,720 0,540" fill="#a82419" opacity="0.55"/>
      <polygon class="band band--black" points="720,0 810,0 810,190 188,812 0,812 0,720" fill="url(#black-fade)"/>
      <polygon class="band band--accent" points="580,0 715,0 650,65 515,65" fill="#f4622a"/>
      <polygon class="chevron chevron--outer" points="625,360 810,175 810,255 705,360 810,465 810,545" fill="url(#chevron-fill)"/>
      <polygon class="chevron chevron--inner" points="735,360 810,285 810,435" fill="#f4582a"/>
    </svg>
    <div class="car-photo" role="img" aria-label="Photo of a red classic muscle car doing a burnout on asphalt, tyre smoke drifting behind it"></div>
    <h1 class="title">
      <span class="title-word title-word--big">Quiet</span>
      <span class="title-word title-word--small">Harbor</span>
      <span class="title-word title-word--big">Drift</span>
    </h1>
    <p class="artist">Marcus Pellworth</p>
  </section>
</main>
</body>
</html>
```